Corwyns Best 4 years in a row

I need a billboard that has all the attached logos and says:

Corwyn's Best Realtor 4 Years in a row!

1.75 Listing Fee

Tobias Wrenfield

555-214-7390

and somewhere very small at the bottom:

855-555-0142

2748 W Amberlow Rd, Linden Vale, OR 20957

I put in the last winner just to give an idea of what I'm looking for, although I'd like to switch it up a little bit.

```html
<!DOCTYPE html>
<html lang="en">
<head>
<meta charset="utf-8">
<title>Corwyn's Best Realtor Billboard</title>
<link rel="stylesheet" href="https://fonts.googleapis.com/css2?family=Oswald:wght@600;700&family=Archivo:ital,wght@0,600;0,800;1,700&display=swap">
<style>
  :root{
    --navy:#13294b;
    --navy-deep:#0e2142;
    --gold:#c9a55a;
    --white:#ffffff;
    --panel:#f4f6f9;
    --backdrop:#e9edf1;
    --photo-a:#b9b4ab;
    --photo-b:#dfe2e4;
  }
  *{margin:0;padding:0;box-sizing:border-box}
  html,body{width:1200px;height:1200px;overflow:hidden;background:var(--backdrop)}
  .billboard{
    position:absolute;left:40px;top:330px;width:1120px;height:540px;
    background:linear-gradient(115deg,var(--white) 0%,var(--panel) 55%,var(--white) 100%);
    overflow:hidden;font-family:'Archivo',sans-serif;
  }
  .billboard__facets{position:absolute;inset:0}
  .agent-photo{
    position:absolute;left:0;top:0;width:560px;height:446px;
    background:linear-gradient(90deg,var(--photo-a) 0%,var(--photo-b) 60%,rgba(255,255,255,0) 100%);
  }
  .headline{
    position:absolute;left:330px;right:40px;top:30px;text-align:center;
    font-family:'Oswald',sans-serif;font-weight:700;font-size:68px;line-height:1;
    color:var(--navy);text-transform:uppercase;letter-spacing:0.5px;white-space:nowrap;
  }
  .headline__sub{
    position:absolute;left:330px;right:40px;top:112px;text-align:center;
    font-style:italic;font-weight:700;font-size:36px;
    color:var(--gold);text-transform:uppercase;white-space:nowrap;
  }
  .fee-badge{position:absolute;left:268px;top:178px;width:240px;height:230px}
  .fee-badge__text{
    position:absolute;left:0;right:0;top:58px;text-align:center;color:var(--white);
    font-weight:800;line-height:1;
  }
  .fee-badge__rate{font-size:50px;display:block}
  .fee-badge__label{font-family:'Oswald',sans-serif;font-weight:600;font-size:30px;display:block;margin-top:8px;line-height:1.05}
  .agent-name{
    position:absolute;left:548px;top:228px;font-weight:800;font-size:52px;line-height:1;
    color:var(--navy);text-transform:uppercase;white-space:nowrap;
  }
  .agent-phone{
    position:absolute;left:548px;top:290px;font-weight:800;font-size:66px;line-height:1;
    color:var(--navy);white-space:nowrap;
  }
  .gold-rule{position:absolute;left:0;right:0;top:446px;height:4px;background:var(--gold)}
  .footer-band{
    position:absolute;left:0;right:0;top:450px;height:90px;background:var(--navy-deep);
    display:flex;align-items:center;padding-left:130px;gap:30px;
  }
  .partner{display:flex;align-items:center;gap:10px;color:var(--white);font-weight:600;font-size:14px;text-transform:uppercase;white-space:nowrap}
  .partner__mark{width:26px;height:26px;border-radius:50%;background:var(--gold);flex:none}
  .partner__mark--square{border-radius:0}
  .partner-badge{width:40px;height:46px;flex:none}
  .footer-contact{margin-left:auto;margin-right:30px;color:var(--white);font-weight:600;line-height:1.5;white-space:nowrap}
  .footer-contact__phone{font-size:18px;display:block}
  .footer-contact__address{font-size:13px;display:block;text-transform:uppercase}
</style>
</head>
<body>
  <main class="billboard">
    <svg class="billboard__facets" width="1120" height="540" aria-hidden="true">
      <polygon points="760,0 1120,0 1120,260 900,446 680,446" fill="#e9edf2" opacity="0.7"/>
      <polygon points="880,0 1120,0 1120,120" fill="#dde3ea" opacity="0.6"/>
    </svg>
    <div class="agent-photo" role="img" aria-label="Photo of smiling realtor in a navy blazer in front of blurred suburban homes"></div>

    <h1 class="headline">Corwyn's Best Realtor</h1>
    <p class="headline__sub">4 Years in a Row!</p>

    <div class="fee-badge">
      <svg width="240" height="230" viewBox="0 0 240 230" aria-hidden="true">
        <polygon points="120,4 228,50 222,168 120,226 18,168 24,50" fill="none" stroke="var(--white)" stroke-width="3"/>
        <polygon points="120,22 212,60 208,170 120,218 32,170 28,60" fill="var(--gold)"/>
        <polygon points="120,32 202,66 198,164 120,208 42,164 38,66" fill="var(--navy)"/>
      </svg>
      <div class="fee-badge__text">
        <span class="fee-badge__rate">1.75%</span>
        <span class="fee-badge__label">LISTING<br>FEE</span>
      </div>
    </div>

    <p class="agent-name">Tobias Wrenfield</p>
    <p class="agent-phone">555-214-7390</p>

    <div class="gold-rule"></div>
    <footer class="footer-band">
      <div class="partner"><span class="partner__mark"></span>Keystone Realty</div>
      <div class="partner"><span class="partner__mark partner__mark--square"></span>Home Guild</div>
      <div class="partner"><span class="partner__mark partner__mark--square"></span>Best Agents</div>
      <svg class="partner-badge" viewBox="0 0 40 46" aria-hidden="true">
        <path d="M20 2 L38 9 V24 C38 35 29 42 20 45 C11 42 2 35 2 24 V9 Z" fill="var(--gold)"/>
      </svg>
      <div class="footer-contact">
        <span class="footer-contact__phone">855-555-0142</span>
        <span class="footer-contact__address">2748 W Amberlow Rd, Linden Vale, OR 20957</span>
      </div>
    </footer>
  </main>
</body>
</html>
```